MOLVT Study flyer

I need help designing a flyer for a research study that will include brain imaging in adolescents. The info is in the attached document. The study is called the Marrowby Orchard Lantern Vesper Trail (MOLVT) study. Ideally this would be returned as a document that I can edit in the future as we will have several new recruitment phases (different age groups, etc. I also would love to have a logo designed as part of this project, but I recognize that might be a separate design request.

```html
<!DOCTYPE html>
<html lang="en">
<head>
<meta charset="utf-8">
<title>MOLVT Study Flyer</title>
<link rel="stylesheet" href="https://fonts.googleapis.com/css2?family=Oswald:wght@500;600&family=Montserrat:wght@400;500;600;700&display=swap">
<style>
  :root {
    --blue: #2f6fb3;
    --ink: #111111;
    --brown: #6a2e0c;
    --orange-soft: #f6c7a4;
    --orange-line: #c26a2a;
    --rule: #4a7fc0;
    --white: #ffffff;
    --page: #ffffff;
  }
  * { box-sizing: border-box; margin: 0; padding: 0; }
  html, body { width: 727px; height: 1200px; overflow: hidden; background: var(--page); }
  .flyer { position: relative; width: 727px; height: 1200px; background: var(--white); font-family: "Montserrat", sans-serif; color: var(--ink); }

  .hero-photo {
    position: absolute; left: 300px; top: 0; width: 427px; height: 580px;
    background:
      linear-gradient(90deg, #ffffff 0%, rgba(255,255,255,0.85) 22%, rgba(255,255,255,0) 55%),
      radial-gradient(ellipse at 55% 55%, #f4f1ec 0%, #dfe6ec 30%, transparent 55%),
      linear-gradient(160deg, #c9d6e0 0%, #aac3d6 40%, #6fa6c9 75%, #2f7fb0 100%);
  }

  .study-name { position: absolute; left: 28px; top: 34px; font-family: "Oswald", sans-serif; font-weight: 600; font-size: 92px; line-height: 1; color: var(--blue); letter-spacing: 1px; }

  .headline { position: absolute; left: 29px; top: 188px; font-family: "Oswald", sans-serif; font-weight: 600; line-height: 1; }
  .headline .lead { display: block; font-size: 38px; color: var(--ink); }
  .headline .age { display: block; font-size: 51px; color: var(--blue); margin-top: 2px; }

  .question { position: absolute; left: 30px; top: 296px; font-size: 23px; font-weight: 500; line-height: 1.2; width: 360px; }
  .intro { position: absolute; left: 30px; top: 416px; width: 330px; font-size: 14.5px; font-weight: 500; line-height: 1.7; }

  .section-title { font-size: 19px; font-weight: 700; line-height: 1.2; }

  .participation { position: absolute; left: 29px; top: 620px; width: 350px; }
  .participation .section-title { margin-bottom: 20px; }
  .step-list { list-style: none; }
  .step { display: flex; align-items: flex-start; gap: 16px; margin-bottom: 14px; font-size: 12px; font-weight: 600; line-height: 1.25; }
  .step-icon { flex: none; width: 32px; height: 32px; border-radius: 50%; background: var(--blue); display: flex; align-items: center; justify-content: center; }

  .illustration { position: absolute; left: 22px; top: 873px; width: 350px; height: 208px; background: radial-gradient(ellipse at 50% 60%, #b7bde0 0%, #d9dcee 35%, #f4f5f8 70%); }

  .divider { position: absolute; left: 412px; top: 614px; width: 1px; height: 436px; background: var(--rule); }

  .eligibility { position: absolute; left: 442px; top: 620px; width: 265px; }
  .eligibility .section-title { margin-bottom: 20px; }
  .criteria { list-style: none; }
  .criterion { display: flex; align-items: flex-start; gap: 12px; margin-bottom: 16px; font-size: 12px; font-weight: 600; line-height: 1.5; }
  .criterion-icon { flex: none; width: 30px; height: 30px; border-radius: 50%; background: var(--orange-soft); display: flex; align-items: center; justify-content: center; margin-top: -3px; }

  .compensation { position: absolute; left: 480px; top: 936px; font-family: "Montserrat", sans-serif; }
  .compensation .label { display: block; font-family: "Oswald", sans-serif; font-weight: 600; font-size: 29px; line-height: 1; color: var(--blue); }
  .compensation .upto { display: block; font-size: 27px; font-weight: 700; line-height: 0.9; }
  .compensation .amount { display: block; font-size: 58px; font-weight: 700; line-height: 1; letter-spacing: -1px; }
  .money-icon { position: absolute; left: 620px; top: 982px; }

  .contact-band { position: absolute; left: 0; bottom: 0; width: 727px; height: 118px; background: var(--brown); color: var(--white); }
  .band-title { position: absolute; font-family: "Oswald", sans-serif; font-weight: 500; font-size: 28px; line-height: 1; }
  .band-text { position: absolute; font-size: 20px; font-weight: 400; }
  .band-left .band-title { left: 30px; top: 36px; }
  .band-left .band-text { left: 30px; top: 76px; }
  .band-right .band-title { left: 418px; top: 36px; }
  .email { position: absolute; left: 458px; top: 78px; display: flex; align-items: center; gap: 6px; font-size: 17px; font-weight: 500; }
</style>
</head>
<body>
<main class="flyer">
  <div class="hero-photo" role="img" aria-label="Photo of a young girl lying on an MRI scanner bed"></div>

  <h1 class="study-name">MOLVT</h1>
  <h2 class="headline"><span class="lead">ARE YOU THE PARENT OF</span><span class="age">A CHILD AGE 10-17?</span></h2>
  <p class="question">Do they worry or overthink negative emotions?</p>
  <p class="intro">Halvern University researchers are seeking girls age 10-17 for a study about brain activity in emotions and deci-sion-making and how they relate to pu-berty, anxiety and depression.</p>

  <section class="participation">
    <h3 class="section-title">Study participation involves :</h3>
    <ul class="step-list">
      <li class="step">
        <span class="step-icon"><svg width="18" height="18" viewBox="0 0 18 18" fill="none" stroke="#fff" stroke-width="1.4"><circle cx="5" cy="5" r="2.5"/><circle cx="13" cy="5" r="2.5"/><path d="M1 15c0-3 2-5 4-5s4 2 4 5M9 15c0-3 2-5 4-5s4 2 4 5"/></svg></span>
        <span>One one-hour interview (online or<br>in-person) where your child will discuss<br>their thoughts</span>
      </li>
      <li class="step">
        <span class="step-icon"><svg width="18" height="18" viewBox="0 0 18 18" fill="none" stroke="#fff" stroke-width="1.4"><rect x="2" y="3" width="14" height="10" rx="1"/><path d="M6 16h6M9 13v3M5 7h8M5 10h5"/></svg></span>
        <span>Online questionnaires<br>(parent and child)</span>
      </li>
      <li class="step">
        <span class="step-icon"><svg width="18" height="18" viewBox="0 0 18 18" fill="none" stroke="#fff" stroke-width="1.4"><circle cx="9" cy="8" r="6"/><circle cx="9" cy="8" r="2.5"/><path d="M2 16h14"/></svg></span>
        <span>One two-hour visit where your child will complete an MRI scan, answer questions about their puberty stage, and have a small hair sample taken to study puberty hormones</span>
      </li>
    </ul>
  </section>

  <div class="illustration" role="img" aria-label="Illustration of a worried teenager holding their head, surrounded by storm clouds and tangled thought bubbles"></div>

  <div class="divider"></div>

  <section class="eligibility">
    <h3 class="section-title">Your child may be<br>eligible if they:</h3>
    <ul class="criteria">
      <li class="criterion">
        <span class="criterion-icon"><svg width="16" height="16" viewBox="0 0 16 16" fill="none" stroke="#8a3f10" stroke-width="1.2"><circle cx="5" cy="5" r="2"/><circle cx="11" cy="5" r="2"/><path d="M1 14c0-3 2-5 4-5s4 2 4 5M7 14c0-3 2-5 4-5s4 2 4 5"/></svg></span>
        <span>Are age 10-17</span>
      </li>
      <li class="criterion">
        <span class="criterion-icon"><svg width="16" height="16" viewBox="0 0 16 16" fill="none" stroke="#8a3f10" stroke-width="1.2"><circle cx="8" cy="6" r="4"/><path d="M6 6h4M8 4v4M4 15c0-2 2-4 4-4s4 2 4 4"/></svg></span>
        <span>Tend to worry or overthink<br>negative thoughts</span>
      </li>
      <li class="criterion">
        <span class="criterion-icon"><svg width="16" height="16" viewBox="0 0 16 16" fill="none" stroke="#8a3f10" stroke-width="1.2"><circle cx="8" cy="7" r="5"/><path d="M6 5l4 4M10 5l-4 4"/></svg></span>
        <span>have not been diagnosed with psychosis, learning problems, or autism Interested in partici-pating? Want more informa-tion? Please contact us!</span>
      </li>
    </ul>
  </section>

  <div class="compensation">
    <span class="label">COMPENSATION</span>
    <span class="upto">up to</span>
    <span class="amount">$140</span>
  </div>
  <svg class="money-icon" width="80" height="70" viewBox="0 0 80 70" aria-hidden="true">
    <path d="M32 6 l8 6 l8-6 l-3 10 h-10 z" fill="#111"/>
    <circle cx="40" cy="34" r="19" fill="#111"/>
    <text x="40" y="42" text-anchor="middle" font-family="Montserrat, sans-serif" font-weight="700" font-size="20" fill="#fff">$</text>
    <path d="M14 58 q20 -10 30 -4 l18 -8 q6 -2 6 4 l-24 16 h-30 z" fill="#111"/>
    <rect x="2" y="52" width="10" height="16" fill="#111"/>
  </svg>

  <footer class="contact-band">
    <div class="band-left">
      <p class="band-title">INTERESTED IN PARTICIPATING ?</p>
      <p class="band-text">Please contact us!</p>
    </div>
    <div class="band-right">
      <p class="band-title">WANT MORE INFORMATION?</p>
      <p class="email">
        <svg width="18" height="13" viewBox="0 0 18 13" aria-hidden="true"><rect x="0.5" y="0.5" width="17" height="12" fill="#fff"/><path d="M1 1l8 6 8-6" fill="none" stroke="#6a2e0c" stroke-width="1.3"/></svg>
        molvtstudy@halvern.edu
      </p>
    </div>
  </footer>
</main>
</body>
</html>
```